Ridgeline Journeys business card

please see website
www.ridgelinejourneys.comau

info needed on card
Kieran Folsby
Ph
email
Adventure Riding GPS trails

please use my logo and colours off my site

Industry/Entity Type

Business

Contact Information for Business Card

Kieran Folsby
kieran@ridgelinejourneys.com

```html
<!DOCTYPE html>
<html lang="en">
<head>
<meta charset="utf-8">
<title>Ridgeline Journeys – Business Card</title>
<link href="https://fonts.googleapis.com/css2?family=Open+Sans:ital,wght@0,400;0,600;0,700;1,400;1,600&display=swap" rel="stylesheet">
<style>
  :root {
    --backdrop: #4a4a4a;
    --card-white: #f7f7f7;
    --ink: #1a1a1a;
    --ink-soft: #3a3a3a;
    --ink-muted: #555555;
    --black: #000000;
    --yellow: #f6d21a;
    --yellow-deep: #f2c200;
  }
  * { box-sizing: border-box; margin: 0; padding: 0; }
  html, body {
    width: 1200px;
    height: 750px;
    overflow: hidden;
    background: var(--backdrop);
    font-family: "Open Sans", sans-serif;
  }
  .canvas {
    position: relative;
    width: 1200px;
    height: 750px;
  }
  .card {
    position: absolute;
    left: 371px;
    width: 461px;
    height: 263px;
    overflow: hidden;
  }
  .card--front { top: 99px; background: var(--card-white); }
  .card--back  { top: 381px; background: var(--black); }

  /* Front: brand lockup */
  .brand {
    position: absolute;
    top: 38px;
    right: 22px;
    display: flex;
    align-items: center;
    gap: 10px;
  }
  .brand__dot {
    width: 34px;
    height: 34px;
    border-radius: 50%;
    background: var(--yellow);
  }
  .brand__name {
    font-weight: 700;
    font-size: 19px;
    color: var(--ink);
    line-height: 1;
  }

  /* Front: contact block */
  .contact {
    position: absolute;
    left: 23px;
    top: 122px;
  }
  .contact__name {
    font-weight: 600;
    font-size: 16.5px;
    color: var(--ink);
    margin-bottom: 10px;
  }
  .contact__list { list-style: none; }
  .contact__item {
    display: flex;
    align-items: center;
    gap: 6px;
    font-size: 11px;
    color: var(--ink-soft);
    height: 18.5px;
  }
  .contact__icon { width: 12px; height: 12px; flex: none; }
  .tagline--front {
    margin-top: 5px;
    font-style: italic;
    font-weight: 600;
    font-size: 13px;
    color: var(--ink-muted);
    letter-spacing: 0.3px;
  }

  /* Front: footer band */
  .band {
    position: absolute;
    left: 0;
    bottom: 0;
    width: 100%;
    height: 18px;
  }

  /* Back */
  .back-brand {
    position: absolute;
    top: 98px;
    left: 0;
    width: 100%;
    display: flex;
    justify-content: center;
    align-items: center;
    gap: 12px;
  }
  .back-brand__dot {
    width: 40px;
    height: 40px;
    border-radius: 50%;
    background: var(--yellow);
  }
  .back-brand__name {
    font-weight: 700;
    font-size: 24px;
    color: var(--yellow);
  }
  .tagline--back {
    position: absolute;
    top: 214px;
    left: 0;
    width: 100%;
    text-align: center;
    font-style: italic;
    font-size: 13px;
    color: var(--yellow);
  }
</style>
</head>
<body>
<main class="canvas">

  <section class="card card--front" aria-label="Business card front">
    <div class="brand">
      <span class="brand__dot"></span>
      <span class="brand__name">Ridgeline Journeys</span>
    </div>

    <div class="contact">
      <h1 class="contact__name">Kieran Folsby</h1>
      <ul class="contact__list">
        <li class="contact__item">
          <svg class="contact__icon" viewBox="0 0 12 12" aria-hidden="true">
            <path d="M2.2 0.8 L4.2 0.6 L5 3.2 L3.7 4.2 Q4.6 6.6 7.1 8.2 L8.2 6.9 L11 7.7 L10.8 9.9 Q10.2 11.3 8.6 11 Q2.6 9.4 0.9 3 Q0.7 1.4 2.2 0.8 Z" fill="#111"/>
          </svg>
          689 512 0947
        </li>
        <li class="contact__item">
          <svg class="contact__icon" viewBox="0 0 12 12" aria-hidden="true">
            <rect x="0.5" y="2" width="11" height="8" fill="#111"/>
            <path d="M0.8 2.4 L6 6.6 L11.2 2.4" stroke="#f7f7f7" stroke-width="1" fill="none"/>
          </svg>
          kieran@ridgelinejourneys.com
        </li>
        <li class="contact__item">
          <svg class="contact__icon" viewBox="0 0 12 12" aria-hidden="true">
            <circle cx="6" cy="6" r="5.5" fill="#111"/>
            <ellipse cx="6" cy="6" rx="2.4" ry="5.3" fill="none" stroke="#f7f7f7" stroke-width="0.8"/>
            <line x1="0.6" y1="6" x2="11.4" y2="6" stroke="#f7f7f7" stroke-width="0.8"/>
          </svg>
          www.ridgelinejourneys.comau
        </li>
      </ul>
      <p class="tagline--front">Adventure Riding GPS trails</p>
    </div>

    <svg class="band" viewBox="0 0 461 18" preserveAspectRatio="none" aria-hidden="true">
      <defs>
        <linearGradient id="bandYellow" x1="0" x2="1" y1="0" y2="0">
          <stop offset="0" stop-color="var(--yellow-deep)"/>
          <stop offset="1" stop-color="var(--yellow)"/>
        </linearGradient>
      </defs>
      <polygon points="0,0 299,0 295,18 0,18" fill="#000"/>
      <polygon points="303,0 461,0 461,18 299,18" fill="url(#bandYellow)"/>
    </svg>
  </section>

  <section class="card card--back" aria-label="Business card back">
    <div class="back-brand">
      <span class="back-brand__dot"></span>
      <span class="back-brand__name">Ridgeline Journeys</span>
    </div>
    <p class="tagline--back">Adventure Riding GPS trails</p>
  </section>

</main>
</body>
</html>
```